Relaunch / redesign online store

We want to refresh our existing online store and have a clear, bright, modern and disgusting template. We are running an online store for fireplaces and chimneys. Our positioning in the market is recognized as a specialist for fireplaces. Due to the fact that the products are costy, we need to send the message that we are trustful. The goal is to make the page look fresh and modern again, without being too posh. In the actual desing there are too many elements like sliders, etc. It is overloaded with information and may overwhelm the user. The elements given in the header and footer, etc. Elements that you can delete are: Tile with "Sure because certified "In it," Save coupon now "," our top sellers for you ", Elements under" Worth knowing ". The store has several types of landing pages. Here is an example for each type of landing page: Home: kolvaro.de Category: https://www.kolvaro.de/kaminofen Product: https://www.kolvaro.de/kaminofen/kaminofen-varnel-dorvin-6 -kw.html Content: https://www.kolvaro.de/kaminofen-aufbauservice-anschluss Please give us an idea of every landing page type. Think about the mobile look of the design. The design has become easy to use for a responsive template. The clickable elements as links, buttons, etc. have to be enough and clear to recognize by the user. Generally speaking, we want to make the site kolvaro.de look up to date again. The actual design is about 10 years old. A modern template should use more of the width of screens. So, the left, font size etc. should be bigger and more up to date looking. So, the design should be less dark than it is now. The colors used for the new look should match the logo color and style but we are not narrowed to some special colors. Here you have space for creativity. Here are some keywords which should match your design: cozy, warm, professional, clear, good price-performance ratio, trustful, state of the art, our target group is 45 years of age. We are looking forward to your design.

Target Market(s)

germany

Number of Pages Required

4 page

Requirements
Must have
• The elements like menu structre, links and content on the pages have as a part of the new design. The sliders are now on the main home can be completely deleted.

```html
<!DOCTYPE html>
<html lang="de">
<head>
<meta charset="utf-8">
<title>kolvaro – Kaminöfen</title>
<link rel="stylesheet" href="https://fonts.googleapis.com/css2?family=Open+Sans:wght@400;600;700;800&family=Oswald:wght@500;600&display=swap">
<style>
:root{
  --orange:#f0901c;
  --orange-deep:#e46c12;
  --orange-light:#f7b33a;
  --ink:#262626;
  --slate:#3b3b3b;
  --grey:#8a8a8a;
  --paper:#ffffff;
  --mist:#ecebe8;
  --rail:rgba(0,0,0,.10);
}
*{box-sizing:border-box;margin:0;padding:0}
html,body{width:1200px;height:3608px;overflow:hidden}
body{position:relative;font-family:"Open Sans",Arial,sans-serif;color:var(--ink);
  background:linear-gradient(180deg,var(--orange) 0,var(--orange-light) 900px,var(--orange-deep) 1900px,var(--orange) 2500px,var(--orange-light) 2760px);}
.abs{position:absolute}

/* rail */
.side-rail{position:absolute;left:0;top:0;width:56px;height:3248px;background:var(--rail);z-index:5}
.side-rail span{position:absolute;left:28px;transform:translateX(-50%) rotate(-90deg);white-space:nowrap;
  font-size:10px;letter-spacing:.12em;text-transform:uppercase;color:rgba(255,255,255,.8)}

/* header + hero */
.hero{position:absolute;left:0;top:0;width:1200px;height:620px;overflow:hidden}
.hero-photo{position:absolute;inset:0;background:linear-gradient(100deg,#2d2d2d 0,#6e6e6e 30%,#9b9b9b 55%,#5c5c5c 75%,#3a3a3a 100%)}
.hero-fire{position:absolute;left:760px;top:110px;width:300px;height:420px;background:radial-gradient(ellipse at 50% 62%,#ffb23a 0,#e4571a 25%,#5a1d0b 55%,#141414 80%);border:10px solid #2a2a2a}
.header-band{position:absolute;left:0;top:0;width:1200px;height:96px;background:linear-gradient(90deg,var(--orange) 0,rgba(240,144,28,.6) 30%,rgba(0,0,0,0) 60%)}
.brand{position:absolute;left:72px;top:26px;font-size:40px;font-weight:700;color:var(--paper);letter-spacing:-.01em}
.hero-brand{position:absolute;left:560px;top:270px;font-size:34px;font-weight:700;color:var(--paper)}
.menu-btn{position:absolute;right:24px;top:26px;width:34px;height:30px}
.hero-caption{position:absolute;left:56px;top:540px;width:1144px;height:80px;background:rgba(20,20,20,.72);padding:14px 0 0 100px;color:var(--paper)}
.hero-caption h1{font-size:20px;font-weight:700}
.hero-caption p{font-size:11px;opacity:.8;margin-top:4px;width:420px}
.hero-caption .more{position:absolute;right:60px;top:44px;font-size:11px;opacity:.8}

/* section labels */
.section-label{position:absolute;left:160px;font-size:12px;font-weight:700;letter-spacing:.06em;text-transform:uppercase;color:var(--ink)}

/* product cards */
.card-row{position:absolute;left:56px;width:1144px;height:368px;overflow:hidden}
.card{position:absolute;top:0;width:210px;height:368px;background:var(--paper);box-shadow:0 4px 14px rgba(0,0,0,.12)}
.card-photo{height:168px;background:linear-gradient(160deg,#f2f0ed 0,#cfcac3 60%,#8d857b 100%)}
.card-photo.warm{background:radial-gradient(ellipse at 50% 60%,#f39a2c 0,#7a3513 30%,#3a3a3a 55%,#e6e3de 80%)}
.card-photo.blue{background:radial-gradient(ellipse at 50% 55%,#3d5b9a 0,#2a3f6e 35%,#e6e3de 70%)}
.card-photo.steel{background:linear-gradient(160deg,#f4f4f4 0,#b9b9b9 50%,#5e5e5e 100%)}
.card-body{position:relative;padding:16px 16px 0 22px}
.card-body::before{content:"";position:absolute;left:0;top:18px;border:8px solid transparent;border-left-color:var(--orange-deep)}
.card h3{font-size:16px;font-weight:800;letter-spacing:.02em;text-transform:uppercase}
.card p{font-size:10px;line-height:1.55;color:var(--grey);margin-top:10px}
.card-foot{position:absolute;left:0;bottom:0;width:100%;height:40px;border-top:1px solid var(--mist);display:flex;align-items:center;padding-left:14px;font-size:10px;color:var(--grey)}
.card-foot i{width:22px;height:16px;background:var(--mist);margin-right:10px;border-radius:2px}
.row-arrow{position:absolute;right:48px;width:28px;height:40px}

/* passion */
.passion{position:absolute;left:56px;top:1140px;width:1144px;height:660px;overflow:hidden}
.passion-photo{position:absolute;inset:0;background:linear-gradient(90deg,#e9e6e2 0,#d8d4cf 20%,#f4f2ef 50%,#e2ded9 100%)}
.passion-stove{position:absolute;left:84px;top:200px;width:170px;height:300px;background:radial-gradient(ellipse at 50% 45%,#f6a12e 0,#c9531a 25%,#262626 50%,#1b1b1b 100%);border-radius:14px 14px 4px 4px}
.passion-title{position:absolute;left:320px;top:250px;font-family:"Oswald",Arial,sans-serif;font-weight:600;font-size:96px;line-height:.92;color:var(--paper);text-shadow:0 2px 10px rgba(0,0,0,.25)}
.go{position:absolute;left:506px;top:300px;width:76px;height:76px;border-radius:50%;border:3px solid var(--paper);background:rgba(40,40,40,.6);color:var(--paper);font-family:"Oswald",Arial,sans-serif;font-size:22px;display:flex;align-items:center;justify-content:center}
.range-list{position:absolute;left:736px;top:228px;width:408px;list-style:none}
.range-list li{height:56px;margin-bottom:18px;background:var(--slate);color:var(--paper);font-size:28px;padding:6px 0 0 16px;position:relative}
.range-list li::after{content:"";position:absolute;right:20px;top:20px;border:8px solid transparent;border-left-color:var(--paper)}
.passion-caption{position:absolute;left:40px;top:540px;color:var(--paper);width:320px}
.passion-caption h2{font-size:20px;font-weight:700}
.passion-caption p{font-size:11px;margin-top:4px;opacity:.9}

/* about text */
.intro{position:absolute;left:160px;top:1840px;width:760px;display:flex;gap:40px;color:var(--ink)}
.intro div{width:360px}
.intro p{font-size:11px;line-height:1.7;margin-bottom:14px}

/* resource columns */
.resources{position:absolute;left:160px;top:2580px;width:960px;display:flex;gap:40px}
.resources div{width:210px}
.resources h4{font-size:17px;font-weight:700;color:var(--ink)}
.resources p{font-size:11px;line-height:1.6;color:var(--paper);margin-top:8px}

/* team */
.team{position:absolute;left:0;top:2768px;width:1200px;height:464px;background:linear-gradient(90deg,#bdbdbd 0,#e8e8e8 30%,#cfcfcf 60%,#8f8f8f 100%)}
.team-stove{position:absolute;left:240px;top:0;width:280px;height:464px;background:radial-gradient(ellipse at 50% 45%,#ffc244 0,#e0671b 22%,#262626 45%,#1c1c1c 100%)}
.team-name{position:absolute;left:700px;top:190px;color:var(--paper)}
.team-name h2{font-size:36px;font-weight:600}
.team-name p{font-size:11px;margin-top:6px;opacity:.9}

/* footer */
.site-footer{position:absolute;left:0;top:3232px;width:1200px;height:376px;background:linear-gradient(180deg,#f3ede6,#e9e2d9)}
.footer-cols{position:absolute;left:160px;top:48px;display:flex;gap:70px}
.footer-cols div{width:150px}
.footer-cols h5{font-size:11px;font-weight:700;text-transform:uppercase;letter-spacing:.06em;margin-bottom:10px}
.footer-cols p,.footer-cols li{font-size:10px;line-height:1.8;color:#6d6d6d;list-style:none}
.copyright{position:absolute;left:160px;top:320px;font-size:10px;color:#8d8d8d;border-top:1px solid #d8d0c6;width:880px;padding-top:10px}
</style>
</head>
<body>

<aside class="side-rail">
  <span style="top:400px">Scroll to explore</span>
  <span style="top:1500px">Stove range</span>
  <span style="top:2680px">Get in touch</span>
</aside>

<header class="hero">
  <div class="hero-photo" role="img" aria-label="Living room with armchair beside a modern stove"></div>
  <div class="hero-fire" role="img" aria-label="Fire burning behind a stove glass door"></div>
  <div class="header-band"></div>
  <div class="brand">kolvaro</div>
  <div class="hero-brand">kolvaro</div>
  <svg class="menu-btn" viewBox="0 0 34 30"><rect width="34" height="30" fill="#3b3b3b"/><path d="M9 10h16M9 15h16M9 20h16" stroke="#fff" stroke-width="2"/></svg>
  <div class="hero-caption">
    <h1>Humble Beginnings</h1>
    <p>Warm rooms begin with a good stove. Find models built to last for many winters.</p>
    <span class="more">Read more</span>
  </div>
</header>

<div class="section-label" style="top:724px">Features worth knowing</div>
<section class="card-row" style="top:772px">
  <article class="card" style="left:-136px"><div class="card-photo steel" role="img" aria-label="Stove product"></div><div class="card-body"><h3>Texture</h3><p>Solid steel body with a wide glass door for a clear view of the flames.</p></div><div class="card-foot"><i></i>View product</div></article>
  <article class="card" style="left:100px"><div class="card-photo warm" role="img" aria-label="Black stove with fire"></div><div class="card-body"><h3>Decayed</h3><p>Solid steel body with a wide glass door for a clear view of the flames.</p></div><div class="card-foot"><i></i>View product</div></article>
  <article class="card" style="left:322px"><div class="card-photo steel" role="img" aria-label="Grey stove"></div><div class="card-body"><h3>Bliss Texture</h3><p>Solid steel body with a wide glass door for a clear view of the flames.</p></div><div class="card-foot"><i></i>View product</div></article>
  <article class="card" style="left:544px"><div class="card-photo warm" role="img" aria-label="Tiled fireplace"></div><div class="card-body"><h3>Decayed</h3><p>Solid steel body with a wide glass door for a clear view of the flames.</p></div><div class="card-foot"><i></i>View product</div></article>
  <article class="card" style="left:766px"><div class="card-photo blue" role="img" aria-label="Blue enamel stove"></div><div class="card-body"><h3>Decayed</h3><p>Solid steel body with a wide glass door for a clear view of the flames.</p></div><div class="card-foot"><i></i>View product</div></article>
  <svg class="row-arrow" style="top:164px" viewBox="0 0 28 40"><path d="M6 4l16 16L6 36" fill="none" stroke="#fff" stroke-width="4"/></svg>
</section>

<section class="passion">
  <div class="passion-photo" role="img" aria-label="Bright kitchen with a black stove"></div>
  <div class="passion-stove" role="img" aria-label="Black stove with burning fire"></div>
  <div class="passion-title">IT'S YOUR<br>PASSION</div>
  <div class="go">GO</div>
  <ul class="range-list">
    <li>Raumluftunabhängig</li>
    <li>wasserführend</li>
    <li>Speicheröfen</li>
    <li>Komplett-Sets</li>
  </ul>
  <div class="passion-caption">
    <h2>Texture makes art</h2>
    <p>Clean lines and honest materials bring calm warmth to every living space.</p>
  </div>
</section>

<section class="intro">
  <div>
    <p>Our stoves are chosen by people who know fire. Each model is tested in our own workshop before it goes on sale, so you can buy with confidence and enjoy many quiet evenings by the flames.</p>
    <p>We advise on size, flue and fitting, and our team can install the stove in your home.</p>
  </div>
  <div>
    <p>Fair prices, free delivery across Germany and a clear warranty make the choice simple. Call us or visit the showroom to see the fire burn before you decide.</p>
  </div>
</section>

<div class="section-label" style="top:2108px">Article worth reading</div>
<section class="card-row" style="top:2148px">
  <article class="card" style="left:-136px"><div class="card-photo warm" role="img" aria-label="Stove product"></div><div class="card-body"><h3>Texture</h3><p>Solid steel body with a wide glass door for a clear view of the flames.</p></div><div class="card-foot"><i></i>View product</div></article>
  <article class="card" style="left:100px"><div class="card-photo warm" role="img" aria-label="Stove with stone panels"></div><div class="card-body"><h3>Decayed</h3><p>Solid steel body with a wide glass door for a clear view of the flames.</p></div><div class="card-foot"><i></i>View product</div></article>
  <article class="card" style="left:322px"><div class="card-photo warm" role="img" aria-label="Black stove with fire"></div><div class="card-body"><h3>Bliss Texture</h3><p>Solid steel body with a wide glass door for a clear view of the flames.</p></div><div class="card-foot"><i></i>View product</div></article>
  <article class="card" style="left:544px"><div class="card-photo warm" role="img" aria-label="Compact stove"></div><div class="card-body"><h3>Decayed</h3><p>Solid steel body with a wide glass door for a clear view of the flames.</p></div><div class="card-foot"><i></i>View product</div></article>
  <article class="card" style="left:766px"><div class="card-photo steel" role="img" aria-label="Steel outdoor grill"></div><div class="card-body"><h3>Decayed</h3><p>Solid steel body with a wide glass door for a clear view of the flames.</p></div><div class="card-foot"><i></i>View product</div></article>
  <svg class="row-arrow" style="top:164px" viewBox="0 0 28 40"><path d="M6 4l16 16L6 36" fill="none" stroke="#fff" stroke-width="4"/></svg>
</section>

<section class="resources">
  <div><h4>Start-Up Resources</h4><p>Guides and checklists to plan your new fireplace step by step at home.</p></div>
  <div><h4>Training &amp; Funding</h4><p>Learn about grants for clean stoves and how to apply for funding today.</p></div>
  <div><h4>Connect</h4><p>Meet our fitters and partners who install stoves in every region of Germany.</p></div>
  <div><h4>Communicate</h4><p>Ask our team anything by phone, mail or chat during the working week.</p></div>
</section>

<section class="team">
  <div class="team-stove" role="img" aria-label="Round black stove with fire in a bright room"></div>
  <div class="team-name">
    <h2>Lena Morwitz</h2>
    <p>Master stove fitter with twenty years of experience in warm homes.</p>
  </div>
</section>

<footer class="site-footer">
  <div class="footer-cols">
    <div><h5>About</h5><p>A family shop for stoves and fireplaces, with a showroom in Germany.</p></div>
    <div><h5>Service</h5><ul><li>Delivery</li><li>Installation</li><li>Warranty</li><li>Returns</li><li>Payment</li></ul></div>
    <div><h5>Shop</h5><ul><li>Stoves</li><li>Fireplaces</li><li>Chimneys</li><li>Accessories</li><li>Sale</li></ul></div>
    <div><h5>Contact</h5><ul><li>Mon–Fri 8–18</li><li>+49 30 5550 1842</li><li>info@kolvaro.de</li></ul></div>
  </div>
  <div class="copyright">© 2024 kolvaro.de · All rights reserved</div>
</footer>

</body>
</html>
```